TBNW site redesign

Please redesign a home page with content provided. PSD only - no coding
Can use any images from Vexelmarq.com

Please create a site design that more clearly illustrates the client's services and expertise. We are looking for a high-end design.

Any images used must be generic or of Dallas TX.

Fonts: Any
Colors: Match to logo
Look: Modern - Professional

Target Market(s)

medium-large business owners

Number of Pages Required

1 page

Font styles to use
Serif
Sans Serif

Requirements
Must have
• cohesive professional design
• high end look
• Match to logo

```html
<!DOCTYPE html>
<html lang="en">
<head>
<meta charset="utf-8">
<title>TBNW – Thornbridge Commercial Realty Group</title>
<link href="https://fonts.googleapis.com/css2?family=Libre+Baskerville:wght@400;700&family=Lato:wght@400;700&display=swap" rel="stylesheet">
<style>
:root{
  --red:#d3302f;
  --magenta:#b0206a;
  --rose:#e4557a;
  --ink:#2b2b2b;
  --text:#555;
  --muted:#888;
  --line:#e2e2e2;
  --grey-bg:#efefef;
  --navy:#262a3a;
  --white:#fff;
  --serif:'Libre Baskerville', Georgia, serif;
  --sans:'Lato', Arial, sans-serif;
}
*{box-sizing:border-box;margin:0;padding:0}
html,body{width:1200px;height:4358px;overflow:hidden}
body{position:relative;background:var(--white);font-family:var(--sans);color:var(--text)}
a{color:inherit;text-decoration:none}

/* brand (name set as text beside a plain square) */
.brand{position:absolute;display:flex;align-items:center;gap:12px}
.brand-square{width:22px;height:22px;background:var(--red);flex:none}
.brand-text{font-family:var(--serif);font-weight:400;color:var(--ink);line-height:1.25}
.brand-text .name{display:block;font-size:28px;letter-spacing:2px}
.brand-text .full{display:block;font-size:10px;letter-spacing:1.5px}

/* header */
.site-header{position:absolute;left:0;top:0;width:1200px;height:134px;background:var(--white)}
.site-header .brand{left:118px;top:24px}
.call{position:absolute;left:876px;top:22px;display:flex;align-items:center;gap:10px;font-size:13px;color:var(--ink)}
.call b{font-weight:700}
.call .ic{width:26px;height:26px;background:var(--red);display:flex;align-items:center;justify-content:center}
.main-nav{position:absolute;left:510px;top:82px;display:flex;gap:34px;font-size:12px;font-weight:700;letter-spacing:.5px;color:var(--ink)}
.main-nav .on{color:var(--red);border-bottom:2px solid var(--red);padding-bottom:12px}

/* hero */
.hero{position:absolute;left:0;top:134px;width:1200px;height:522px;background:linear-gradient(180deg,#4b5f9b 0%,#8a87b8 35%,#d9a07a 60%,#3b4a6a 80%,#252d40 100%)}
.hero-box{position:absolute;left:165px;top:196px;width:390px;height:170px;background:rgba(30,34,44,.82);padding:28px 36px}
.hero-box h1{font-family:var(--serif);font-weight:400;font-size:20px;line-height:1.4;color:var(--white)}
.hero-box p{font-size:14px;line-height:1.5;color:#e6e6e6;margin-top:12px}
.hero-arrow{position:absolute;top:238px}

/* about */
.about-title{position:absolute;left:122px;top:760px;font-family:var(--serif);font-weight:400;font-size:44px;line-height:1.15;color:var(--ink)}
.about-title span{color:var(--red)}
.about-rule{position:absolute;left:122px;top:880px;width:150px;height:1px;background:var(--line)}
.about-text{position:absolute;left:343px;top:718px;width:385px;font-size:13px;line-height:1.75;color:var(--text)}
.more{display:inline-block;margin-top:10px;font-family:var(--serif);font-size:11px;color:var(--red);letter-spacing:.5px}
.about-photo{position:absolute;left:778px;top:724px;width:302px;height:190px;background:linear-gradient(135deg,#c9d3de,#8b98a9 60%,#e5c79a)}

/* why */
.why-shape{position:absolute;left:860px;top:1025px}
.why-title{position:absolute;left:960px;top:1270px;width:160px;text-align:center;font-family:var(--serif);font-size:26px;line-height:1.6;letter-spacing:1px;color:var(--white)}
.feature{position:absolute;width:300px;text-align:center}
.feature h3{font-family:var(--serif);font-weight:400;font-size:13px;letter-spacing:1px;color:var(--ink);margin-top:8px}
.feature p{font-size:12px;line-height:1.5;color:var(--text);margin-top:4px}
.feature p em{color:var(--red);font-style:normal}
.v-rule{position:absolute;left:424px;width:1px;background:var(--line)}

/* video */
.intro-line{position:absolute;left:220px;top:1772px;width:760px;text-align:center;font-size:19px;line-height:1.6;color:var(--ink);font-weight:700}
.video-frame{position:absolute;left:116px;top:1850px;width:964px;height:412px;border:1px solid #ddd;box-shadow:0 2px 8px rgba(0,0,0,.15);padding:16px;background:var(--white)}
.video{position:relative;width:100%;height:100%;background:linear-gradient(135deg,#4e5157,#8c8f95 55%,#3c3e44)}
.play{position:absolute;left:50%;top:50%;transform:translate(-50%,-50%)}
.btn{position:absolute;left:510px;top:2298px;width:180px;height:36px;background:var(--red);color:var(--white);font-size:12px;font-weight:700;letter-spacing:.5px;display:flex;align-items:center;justify-content:center}

/* team */
.team-shape{position:absolute;left:0;top:2335px}
.team-title{position:absolute;left:120px;top:2630px;width:155px;text-align:center;font-family:var(--serif);font-size:26px;line-height:1.6;letter-spacing:1px;color:var(--white)}
.team-intro{position:absolute;left:398px;top:2490px;width:682px;text-align:center;font-size:12.5px;line-height:1.75;color:var(--text)}
.member{position:absolute;top:2626px;width:210px;text-align:center}
.member .photo{width:210px;height:215px}
.member h4{font-family:var(--sans);font-size:15px;color:var(--ink);margin-top:16px}
.member p{font-size:11px;font-style:italic;color:var(--muted);margin-top:6px;line-height:1.4}

/* testimonials */
.sec-title{position:absolute;left:0;width:1200px;text-align:center;font-family:var(--serif);font-weight:400;font-size:30px;color:var(--ink);letter-spacing:1px}
.sec-title span{color:var(--red)}
.sec-rule{position:absolute;left:555px;width:90px;height:1px;background:#ccc}
.quote{position:absolute;left:200px;top:3155px;width:800px;text-align:center;font-size:13px;font-style:italic;line-height:1.75;color:var(--text)}
.quote-mark{font-family:var(--serif);font-size:40px;color:#ccc;line-height:0;vertical-align:-14px;margin-right:6px}
.quote-by{position:absolute;left:0;top:3245px;width:1200px;text-align:center;font-family:var(--serif);font-size:14px;color:var(--red)}
.t-arrow{position:absolute;top:3190px}

/* articles */
.articles{position:absolute;left:0;top:3320px;width:1200px;height:558px;background:var(--grey-bg)}
.card{position:absolute;top:3469px;width:296px}
.card .img{position:relative;height:142px}
.date{position:absolute;left:0;top:0;width:50px;height:52px;background:var(--red);color:var(--white);text-align:center;font-size:20px;line-height:1;padding-top:7px}
.date small{display:block;font-size:10px;margin-top:3px}
.card h4{font-size:16px;font-weight:400;color:var(--ink);margin-top:18px}
.meta{display:flex;gap:14px;font-size:11px;color:var(--muted);margin-top:10px;align-items:center}
.meta i{display:inline-block;width:10px;height:10px;background:var(--red);margin-right:5px;vertical-align:-1px}
.card p{font-size:12px;line-height:1.55;color:var(--text);margin-top:10px}
.dots{position:absolute;left:583px;top:3803px;display:flex;gap:6px}
.dots span{width:10px;height:10px;border-radius:50%;border:1px solid var(--red)}
.dots span.on{background:var(--red)}

/* footer */
.site-footer{position:absolute;left:0;top:3878px;width:1200px;height:433px;background:var(--navy);color:#cfd2da}
.f-head{position:absolute;top:50px;font-size:14px;font-weight:700;color:var(--white);letter-spacing:.5px}
.f-list{position:absolute;top:84px;list-style:none;font-size:12px;line-height:2.1}
.f-contact{position:absolute;left:293px;top:84px;font-size:12px;line-height:1.7}
.f-contact div{display:flex;gap:10px;align-items:center;margin-bottom:12px}
.map{position:absolute;left:558px;top:90px;width:267px;height:152px;background:linear-gradient(135deg,#e9ecef,#d6dbe2)}
.site-footer .brand{left:890px;top:140px}
.site-footer .brand-text{color:var(--white)}
.f-legal{position:absolute;left:0;top:310px;width:1200px;text-align:center;font-size:12px;line-height:2.55;color:var(--white);text-decoration:underline}
.f-divider{position:absolute;left:122px;top:285px;width:958px;height:1px;background:#3a3f52}
.bottom-bar{position:absolute;left:0;top:4311px;width:1200px;height:47px;background:var(--red);color:var(--white);font-size:11px}
.bottom-bar .copy{position:absolute;left:122px;top:16px}
.social{position:absolute;left:990px;top:12px;display:flex;gap:6px}
.social span{width:22px;height:22px;border-radius:50%;background:#2a57b7;border:1px solid var(--white)}
</style>
</head>
<body>

<header class="site-header">
  <div class="brand">
    <span class="brand-square"></span>
    <div class="brand-text"><span class="name">TBNW</span><span class="full">THORNBRIDGE COMMERCIAL REALTY GROUP</span></div>
  </div>
  <div class="call">
    <span class="ic"><svg width="14" height="14" viewBox="0 0 24 24"><path fill="#fff" d="M6.6 10.8a15 15 0 006.6 6.6l2.2-2.2c.3-.3.7-.4 1-.2 1.1.4 2.3.6 3.6.6.6 0 1 .4 1 1V20c0 .6-.4 1-1 1A17 17 0 013 4c0-.6.4-1 1-1h3.5c.6 0 1 .4 1 1 0 1.3.2 2.5.6 3.6.1.3 0 .7-.2 1z"/></svg></span>
    <span>Call Today: <b>214-555-0142</b></span>
  </div>
  <nav class="main-nav">
    <a class="on">HOME</a><a>ABOUT TBNW</a><a>SERVICES</a><a>BLOG</a><a>MARKET NEWS</a><a>CONTACT US</a>
  </nav>
</header>

<section class="hero" role="img" aria-label="Dallas downtown skyline at sunset">
  <svg class="hero-arrow" style="left:88px" width="30" height="50" viewBox="0 0 30 50"><path d="M24 4L6 25l18 21" fill="none" stroke="#fff" stroke-width="2"/></svg>
  <svg class="hero-arrow" style="left:1080px" width="30" height="50" viewBox="0 0 30 50"><path d="M6 4l18 21L6 46" fill="none" stroke="#fff" stroke-width="2"/></svg>
  <div class="hero-box">
    <h1>PROFESSIONAL OFFICE AND<br>WAREHOUSE LEASING</h1>
    <p>Fast-track your search with tenant reps that only serve you, and specialize in the DFW area.</p>
  </div>
</section>

<section class="about">
  <h2 class="about-title">ABOUT<br><span>TBNW</span></h2>
  <div class="about-rule"></div>
  <div class="about-text">
    Lorem ipsum dolor sit amet, consectetur adipiscing elit, sed do eiusmod tempor incididunt ut labore et dolore magna aliqua. Ut enim ad minim veniam, quis nostrud exercitation ullamco laboris nisi ut aliquip ex ea commodo consequat. Duis aute irure dolor in reprehenderit in voluptate velit esse cillum dolore eu fugiat nulla pariatur. Excepteur sint occaecat cupidatat non proident, sunt in culpa qui officia deserunt mollit anim id est laborum
    <br><a class="more">LEARN MORE →</a>
  </div>
  <div class="about-photo" role="img" aria-label="Upward view of glass office towers"></div>
</section>

<section class="why">
  <svg class="why-shape" width="340" height="760" viewBox="0 0 340 760">
    <defs><linearGradient id="whyGrad" x1="0" y1="0" x2="1" y2="1"><stop offset="0" stop-color="#e4557a"/><stop offset=".5" stop-color="#b0206a"/><stop offset="1" stop-color="#d7507a"/></linearGradient></defs>
    <path d="M340 0C150 40 10 200 10 380s140 340 330 380z" fill="url(#whyGrad)"/>
  </svg>
  <div class="why-title">WHY<br>TENANT<br>REPRESEN<br>TATION?</div>

  <div class="feature" style="left:90px;top:1180px">
    <svg width="52" height="44" viewBox="0 0 52 44"><g fill="#2d3a52"><circle cx="26" cy="10" r="7"/><circle cx="10" cy="18" r="5"/><circle cx="42" cy="18" r="5"/><path d="M14 40c0-9 5-16 12-16s12 7 12 16z"/><path d="M2 38c0-6 3-11 8-11 2 0 3 .5 4 1.5-2 3-3 6-3 9.5zM50 38c0-6-3-11-8-11-2 0-3 .5-4 1.5 2 3 3 6 3 9.5z"/></g></svg>
    <h3>RELATIONSHIPS</h3>
    <p>Save time by trusting TBNW your after<br>you to find the right location for ... <em>[+]</em></p>
  </div>
  <div class="feature" style="left:454px;top:1180px">
    <svg width="44" height="44" viewBox="0 0 44 44"><circle cx="22" cy="22" r="20" fill="none" stroke="#2d3a52" stroke-width="2"/><rect x="14" y="20" width="16" height="12" fill="none" stroke="#2d3a52" stroke-width="2"/><path d="M17 20v-4a5 5 0 0110 0v4" fill="none" stroke="#2d3a52" stroke-width="2"/></svg>
    <h3>ACCESS TO MORE</h3>
    <p>We have no agreement or personal<br>incentives for specific properties ... <em>[+]</em></p>
  </div>
  <div class="v-rule" style="top:1185px;height:140px"></div>
  <div class="v-rule" style="top:1390px;height:140px"></div>
  <div class="feature" style="left:90px;top:1395px">
    <svg width="44" height="44" viewBox="0 0 44 44"><g fill="#2d3a52"><circle cx="22" cy="13" r="9"/><path d="M4 42c0-11 8-18 18-18s18 7 18 18z"/></g></svg>
    <h3>FREE TO YOU</h3>
    <p>You pay us nothing. We get our commission<br>from the property being leased ... <em>[+]</em></p>
  </div>
  <div class="feature" style="left:454px;top:1395px">
    <svg width="48" height="44" viewBox="0 0 48 44"><g fill="#2d3a52"><rect x="18" y="4" width="14" height="14"/><path d="M2 28h8l10 4h10c2 0 2 4 0 4H20v2h12l12-8c2-1 4 1 2 3L32 42H10l-8-4z"/></g></svg>
    <h3>CUSTOMIZED SERVICE</h3>
    <p>Aside from saving you the time of repeating<br>what your needs are to each new ... <em>[+]</em></p>
  </div>
</section>

<p class="intro-line">If you need to find office or warehouse space in the Dallas Fort Worth area, the team<br>at TBNW has the experience you need.</p>
<div class="video-frame">
  <div class="video" role="img" aria-label="Video still of a hand using a tablet in a warehouse">
    <svg class="play" width="54" height="54" viewBox="0 0 54 54"><circle cx="27" cy="27" r="26" fill="rgba(255,255,255,.85)"/><path d="M22 16l16 11-16 11z" fill="#555"/></svg>
  </div>
</div>
<a class="btn">SPACE CALCULATOR</a>

<section class="team">
  <svg class="team-shape" width="400" height="755" viewBox="0 0 400 755">
    <defs><linearGradient id="teamGrad" x1="0" y1="0" x2="1" y2="1"><stop offset="0" stop-color="#b0206a"/><stop offset=".6" stop-color="#cf3e72"/><stop offset="1" stop-color="#e4557a"/></linearGradient></defs>
    <path d="M0 0c210 40 370 190 370 378S210 715 0 755z" fill="url(#teamGrad)"/>
  </svg>
  <div class="team-title">MEET<br>THE<br>TEAM</div>
  <p class="team-intro">At TBNW we believe that you deserve the best professional advice and personal service with your commercial real estate negotiations. By choosing TBNW as your tenant reps in the Dallas/Fort Worth area, you will receive the assistance of accomplished and experienced commercial real estate brokers and salespeople who are licensed by the State Realty Licensing Board to practice in Texas since 1982.</p>
  <div class="member" style="left:395px">
    <div class="photo" role="img" aria-label="Team member portrait in a warehouse" style="background:linear-gradient(160deg,#c9b08a,#8a6a48 60%,#e2863a)"></div>
    <h4>Graham T. Whitfield</h4>
    <p>Founder and President</p>
  </div>
  <div class="member" style="left:630px">
    <div class="photo" role="img" aria-label="Team member portrait in a warehouse" style="background:linear-gradient(160deg,#d8c79a,#b59a62 55%,#9cb7d6)"></div>
    <h4>Evan Carter-Hale</h4>
    <p>Senior Director, Commercial<br>Property Specialist</p>
  </div>
  <div class="member" style="left:871px">
    <div class="photo" role="img" aria-label="Team member portrait in a warehouse" style="background:linear-gradient(160deg,#a88a6a,#6a5440 55%,#3e78b5)"></div>
    <h4>Marcus Allen Reed</h4>
    <p>Jr. Associate, Tenant Rep Specialist</p>
  </div>
</section>

<section class="testimonials">
  <h2 class="sec-title" style="top:3080px">CLIENT <span>TESTIMONIALS</span></h2>
  <div class="sec-rule" style="top:3130px"></div>
  <svg class="t-arrow" style="left:100px" width="20" height="36" viewBox="0 0 20 36"><path d="M16 2L3 18l13 16" fill="none" stroke="#aaa" stroke-width="2"/></svg>
  <svg class="t-arrow" style="left:1078px" width="20" height="36" viewBox="0 0 20 36"><path d="M4 2l13 16L4 34" fill="none" stroke="#aaa" stroke-width="2"/></svg>
  <p class="quote"><span class="quote-mark">“</span>The real estate team at TBNW has decades of experience in Commercial. One advantage of TBNW is they know all the properties that are about to become available, BEFORE they are available. They have the inside track on properties and they watch your back at the negotiating table. Very impressive with a polished approach. Let the team run with your next project and you won't be disappointed</p>
  <p class="quote-by">– Nathan James Corley</p>
</section>

<section class="articles">
  <h2 class="sec-title" style="top:48px">RECENT <span>ARTICLES</span></h2>
  <div class="sec-rule" style="top:98px;background:#bbb"></div>
</section>
<article class="card" style="left:122px">
  <div class="img" role="img" aria-label="Desk with charts and documents" style="background:linear-gradient(135deg,#e7edf2,#a9bfd3 60%,#5f84a8)"><div class="date">07<small>May<br>2016</small></div></div>
  <h4>Lorem ipsum dolor sit amet, consectetu</h4>
  <div class="meta"><span><i></i>Dana Kessler</span><span><i></i>3 Comments</span></div>
  <p>Adipiscing elit, sd diam nonummy nibh euismod tincid unt ut laoreet sit diam nonummy nibh euismod tincidunt ut laoreet dolore ...[+]</p>
</article>
<article class="card" style="left:450px">
  <div class="img" role="img" aria-label="Businessman in an office" style="background:linear-gradient(135deg,#9aa7b4,#5b6572 55%,#c6a57f)"><div class="date">07<small>May<br>2016</small></div></div>
  <h4>Lorem ipsum dolor sit amet, consectetu</h4>
  <div class="meta"><span><i></i>Dana Kessler</span><span><i></i>3 Comments</span></div>
  <p>Adipiscing elit, sd diam nonummy nibh euismod tincid unt ut laoreet sit diam nonummy nibh euismod tincidunt ut laoreet dolore ...[+]</p>
</article>
<article class="card" style="left:776px">
  <div class="img" role="img" aria-label="Colleagues talking in a bright office" style="background:linear-gradient(135deg,#e9e2d6,#c7b497 55%,#8e7d66)"><div class="date">07<small>May<br>2016</small></div></div>
  <h4>Lorem ipsum dolor sit amet, consectetu</h4>
  <div class="meta"><span><i></i>Dana Kessler</span><span><i></i>3 Comments</span></div>
  <p>Adipiscing elit, sd diam nonummy nibh euismod tincid unt ut laoreet sit diam nonummy nibh euismod tincidunt ut laoreet dolore ...[+]</p>
</article>
<div class="dots"><span class="on"></span><span></span><span></span></div>

<footer class="site-footer">
  <h5 class="f-head" style="left:122px">QUICK LINKS</h5>
  <ul class="f-list" style="left:122px">
    <li>• Home</li><li>• About TBNW</li><li>• Services</li><li>• Blog</li><li>• Market News</li><li>• Contact Us</li>
  </ul>
  <h5 class="f-head" style="left:293px">CONTACT INFORMATION</h5>
  <div class="f-contact">
    <div>410 Cedar Ridge Avenue, Suite 620,<br>Dallas, TX 75204</div>
    <div><svg width="12" height="12" viewBox="0 0 24 24"><path fill="#cfd2da" d="M6.6 10.8a15 15 0 006.6 6.6l2.2-2.2c.3-.3.7-.4 1-.2 1.1.4 2.3.6 3.6.6.6 0 1 .4 1 1V20c0 .6-.4 1-1 1A17 17 0 013 4c0-.6.4-1 1-1h3.5c.6 0 1 .4 1 1 0 1.3.2 2.5.6 3.6.1.3 0 .7-.2 1z"/></svg>214-555-0142</div>
    <div><svg width="12" height="12" viewBox="0 0 24 24"><rect x="3" y="8" width="18" height="10" fill="#cfd2da"/><rect x="7" y="3" width="10" height="5" fill="#cfd2da"/></svg>214-555-0187</div>
    <div><svg width="12" height="12" viewBox="0 0 24 24"><rect x="2" y="5" width="20" height="14" fill="#cfd2da"/><path d="M2 5l10 8 10-8" fill="none" stroke="#262a3a" stroke-width="2"/></svg>info@tbnw.com</div>
  </div>
  <h5 class="f-head" style="left:558px">LOCATION MAP</h5>
  <div class="map" role="img" aria-label="Street map showing the office location">
    <svg style="position:absolute;left:122px;top:52px" width="22" height="30" viewBox="0 0 22 30"><path d="M11 0a11 11 0 0111 11c0 8-11 19-11 19S0 19 0 11A11 11 0 0111 0z" fill="#d3302f"/><circle cx="11" cy="11" r="4" fill="#fff"/></svg>
  </div>
  <div class="brand">
    <span class="brand-square"></span>
    <div class="brand-text"><span class="name">TBNW</span><span class="full">THORNBRIDGE COMMERCIAL REALTY GROUP</span></div>
  </div>
  <div class="f-divider"></div>
  <div class="f-legal">
    State Realty Licensing Board Mandated Disclosure Notices<br>
    State Realty Licensing Board Information About Brokerage Services<br>
    State Realty Licensing Board Consumer Protection Notice
  </div>
</footer>
<div class="bottom-bar">
  <span class="copy">Copyright © 2016 TBNW. All Right Reserved.</span>
  <div class="social" aria-label="Social media links"><span></span><span></span><span></span></div>
</div>

</body>
</html>
```